Nobre Lente Lusitana - business card

Create a business card for my eyewear (glasses) store. The concept is based in handcrafted glasses (as well as common frames and 3d printed), clean, and elegant. The business card could be black (white letters and symbols) or white (black letters and symbols) but we are open to new suggestions. It must be sober and elegant.
The name Nobre Lente Lusitana means Royal/Real Portuguese Optical Store.
Our concept should be inspired by the pictures attatched bellow.
I would like it to be classic and elegant as business cards for bankers.
Our first selected logo is also available in attachment files.

Target Market(s)

For business meetings with investors, supliers and fairs

Industry/Entity Type

Eyewear

Contact Information for Business Card

Some random business cards in attachment that we like. Don't be closed to it, we like freedom of think.

Font styles to use
Serif
Sans Serif

Colors
404040
e9e9e9
fbfbfb
000000
85abd3
0255a3
f7fbfd
959595

Requirements
Must have
• Must be elegant, simple.
• Must present our brand new logo (slight variations are welcome, the logo is not closed yet). See our temporary logo in attachment.
• Black (or dark grey), white (or light grey) and a third slight color.
• This third slight color could be dark blue or grayish blue.
• Info:
• Tomás Vidigal (name)
• tvidigal@nobrelentelusitana.example
• +351 927364051
• www.nobrelentelusitana.example
Nice to have
• Black and white or with serious colors such as dark blue or greyish blue.
• Could also have water mark with our logo (big size) in the background (inspired in KMT bank credit card design)
Should not have
• Hysteric colora or shapes

```html
<!DOCTYPE html>
<html lang="pt">
<head>
<meta charset="utf-8">
<title>Nobre Lente Lusitana – Cartão de visita</title>
<link rel="stylesheet" href="https://fonts.googleapis.com/css2?family=Cinzel:wght@400&family=Montserrat:wght@400;500&display=swap">
<style>
  :root {
    --stage: #e4e4e4;
    --card: #fbfbfb;
    --damask: #f2f2f2;
    --ink: #1a1a1a;
    --band: #404040;
    --band-text: #ffffff;
    --rule: #404040;
    --ornament: #3a3a3a;
  }
  * { box-sizing: border-box; margin: 0; padding: 0; }
  html, body { width: 1200px; height: 800px; overflow: hidden; }
  body {
    background: var(--stage);
    font-family: "Montserrat", Arial, sans-serif;
    color: var(--ink);
    position: relative;
  }
  .card {
    position: absolute;
    top: 214px;
    width: 470px;
    height: 268px;
    background: var(--card);
    box-shadow: 0 1px 3px rgba(0,0,0,.18);
    overflow: hidden;
  }
  .card--front { left: 96px; }
  .card--back { left: 633px; }
  .damask-field {
    position: absolute;
    inset: 0;
    background: radial-gradient(ellipse at center, var(--damask) 0%, var(--card) 85%);
  }
  .frame {
    position: absolute;
    left: 6px; right: 6px; top: 4px; bottom: 4px;
    border-top: 1px solid var(--rule);
    border-bottom: 1px solid var(--rule);
  }
  .frame::before, .frame::after {
    content: "";
    position: absolute;
    top: 26px; bottom: 26px;
    border-left: 1px solid var(--rule);
  }
  .frame::before { left: 0; }
  .frame::after { right: 0; }
  .corner-ornament {
    position: absolute;
    width: 26px; height: 26px;
    background: var(--ornament);
    border-radius: 40%;
    opacity: .85;
  }
  .corner-ornament--tl { left: 6px; top: 4px; }
  .corner-ornament--tr { right: 6px; top: 4px; }
  .corner-ornament--bl { left: 6px; bottom: 4px; }
  .corner-ornament--br { right: 6px; bottom: 4px; }

  .brand-name {
    position: absolute;
    left: 0; right: 0;
    text-align: center;
    font-weight: 500;
    color: var(--ink);
    letter-spacing: .04em;
  }
  .card--front .brand-name { top: 62px; font-size: 14px; }
  .holder {
    position: absolute;
    left: 124px; width: 222px;
    top: 96px;
    border-top: 1px solid var(--rule);
    border-bottom: 1px solid var(--rule);
    height: 25px;
    font-family: "Cinzel", Georgia, serif;
    font-size: 19px;
    line-height: 23px;
    text-align: center;
    color: #2a2a2a;
    letter-spacing: .03em;
  }
  .name-flourish {
    position: absolute;
    left: 178px; top: 127px;
    width: 116px; height: 22px;
    background: linear-gradient(90deg, transparent, #555 30%, #555 70%, transparent);
    opacity: .35;
    border-radius: 10px;
  }
  .contact-band {
    position: absolute;
    left: 6px; right: 6px;
    top: 164px; height: 68px;
    background: var(--band);
    color: var(--band-text);
    font-size: 10.5px;
  }
  .contact-row {
    position: absolute;
    left: 0; right: 0;
    height: 16px;
  }
  .contact-row svg {
    position: absolute;
    left: 117px; top: 2px;
    width: 11px; height: 11px;
  }
  .contact-row span {
    position: absolute;
    left: 130px; right: 0;
    text-align: center;
    padding-right: 100px;
    line-height: 16px;
  }
  .contact-row--phone { top: 8px; }
  .contact-row--mail { top: 25px; }
  .contact-row--web { top: 42px; }

  .card--back .brand-name { top: 150px; font-size: 21px; }
  .card--back .brand-mark {
    position: absolute;
    left: 223px; top: 112px;
    width: 24px; height: 24px;
    border: 2px solid var(--ink);
    border-radius: 50%;
  }
  .back-url {
    position: absolute;
    left: 0; right: 0;
    top: 250px;
    text-align: center;
    font-size: 10.5px;
    color: #2a2a2a;
  }
</style>
</head>
<body>

<section class="card card--front" aria-label="Frente do cartão">
  <div class="damask-field" role="img" aria-label="Padrão damasco suave em cinza claro"></div>
  <div class="frame"></div>
  <div class="corner-ornament corner-ornament--tl" role="img" aria-label="Ornamento flor-de-lis de canto"></div>
  <div class="corner-ornament corner-ornament--tr" role="img" aria-label="Ornamento flor-de-lis de canto"></div>
  <div class="corner-ornament corner-ornament--bl" role="img" aria-label="Ornamento flor-de-lis de canto"></div>
  <div class="corner-ornament corner-ornament--br" role="img" aria-label="Ornamento flor-de-lis de canto"></div>

  <p class="brand-name">NOBRE LENTE LUSITANA</p>
  <h1 class="holder">Tomás Vidigal</h1>
  <div class="name-flourish" role="img" aria-label="Floreado ornamental sob o nome"></div>

  <div class="contact-band">
    <div class="contact-row contact-row--phone">
      <svg viewBox="0 0 12 12" aria-hidden="true"><path d="M2.5 1 L4.5 1 L5 3.5 L3.8 4.3 Q4.8 6.8 7.7 8.2 L8.5 7 L11 7.5 L11 9.5 Q10.5 11 9 11 Q1 10 1 2.5 Q1 1 2.5 1 Z" fill="#fff"/></svg>
      <span>+351 927364051</span>
    </div>
    <div class="contact-row contact-row--mail">
      <svg viewBox="0 0 12 12" aria-hidden="true"><rect x="1" y="2.5" width="10" height="7" fill="#fff"/><path d="M1 2.5 L6 6.5 L11 2.5" stroke="#404040" fill="none"/></svg>
      <span>tvidigal@nobrelentelusitana.example</span>
    </div>
    <div class="contact-row contact-row--web">
      <svg viewBox="0 0 12 12" aria-hidden="true"><circle cx="6" cy="6" r="5" fill="none" stroke="#fff"/><ellipse cx="6" cy="6" rx="2" ry="5" fill="none" stroke="#fff"/><path d="M1 6 H11" stroke="#fff"/></svg>
      <span>www.nobrelentelusitana.example</span>
    </div>
  </div>
</section>

<section class="card card--back" aria-label="Verso do cartão">
  <div class="damask-field" role="img" aria-label="Padrão damasco suave em cinza claro"></div>
  <div class="brand-mark"></div>
  <p class="brand-name">NOBRE LENTE LUSITANA</p>
  <p class="back-url">www.nobrelentelusitana.example</p>
</section>

</body>
</html>
```